Business card for job seeker professional

Hi. I'm a sale and marketing professional who's just moved to Australia and looking for a job. I would like to have a business card designed for me, which I can use for job interviews/networking. Given Pravolink increasing importance in the job market, I would like my public profile link (http://au.pravolink-net.com/in/tomasveridun/) to be incorporated into my details.

```html
<!DOCTYPE html>
<html lang="en">
<head>
<meta charset="utf-8">
<title>Tomas Veridun – Business Card</title>
<link rel="stylesheet" href="https://fonts.googleapis.com/css2?family=Tenor+Sans&family=Lato:wght@400;700&display=swap">
<style>
  :root {
    --backdrop: #ebebe8;
    --card-white: #ffffff;
    --brand-green: #1d6a39;
    --chart-green-soft: #cfe3d3;
    --chart-fade: #f4f4f2;
    --ink: #1a1a1a;
    --profile-blue: #1b5e98;
    --name-white: #ffffff;
  }
  * { box-sizing: border-box; margin: 0; padding: 0; }
  html, body {
    width: 1200px;
    height: 828px;
    overflow: hidden;
    background: var(--backdrop);
  }
  .canvas {
    position: relative;
    width: 1200px;
    height: 828px;
  }
  .business-card {
    position: absolute;
    left: 100px;
    top: 129px;
    width: 1000px;
    height: 570px;
    background: var(--card-white);
    box-shadow: 0 6px 22px rgba(0, 0, 0, 0.18);
    overflow: hidden;
  }
  .name-band {
    height: 221px;
    background: var(--brand-green);
    display: flex;
    align-items: center;
    justify-content: center;
    padding-top: 8px;
  }
  .holder-name {
    font-family: "Tenor Sans", sans-serif;
    font-weight: 400;
    font-size: 56px;
    color: var(--name-white);
  }
  .specialties {
    margin-top: 14px;
    text-align: center;
    font-family: "Lato", sans-serif;
    font-weight: 700;
    font-size: 17px;
    color: var(--ink);
  }
  .contact-details {
    position: absolute;
    left: 25px;
    top: 330px;
    font-family: "Lato", sans-serif;
    color: var(--brand-green);
    line-height: 1;
  }
  .contact-details .location,
  .contact-details .phone {
    font-size: 31px;
    margin-bottom: 12px;
  }
  .contact-details .email {
    font-size: 27px;
  }
  .profile-link {
    position: absolute;
    left: 25px;
    top: 513px;
    display: flex;
    align-items: center;
    gap: 10px;
    font-family: "Lato", sans-serif;
    font-size: 26px;
    color: var(--profile-blue);
    white-space: nowrap;
  }
  .profile-link .network-square {
    width: 42px;
    height: 42px;
    background: var(--profile-blue);
    border-radius: 4px;
    flex: none;
  }
  .growth-chart-area {
    position: absolute;
    left: 725px;
    top: 310px;
    width: 255px;
    height: 240px;
    background: linear-gradient(to top right, var(--chart-fade) 0%, var(--chart-green-soft) 100%);
    border-radius: 6px;
  }
</style>
</head>
<body>
<main class="canvas">
  <article class="business-card">
    <header class="name-band">
      <h1 class="holder-name">Tomas Veridun</h1>
    </header>
    <p class="specialties">Business Strategy | International Business Development | Marketing and Communication</p>

    <section class="contact-details">
      <p class="location">Melbourne, Australia</p>
      <p class="phone">0411 555 019</p>
      <p class="email">tomas@veridun.au</p>
    </section>

    <p class="profile-link">
      <span class="network-square" aria-hidden="true"></span>
      <span class="network-name">Pravolink</span>
      <span class="profile-url">au.pravolink-net.com/in/tomasveridun</span>
    </p>

    <div class="growth-chart-area" role="img" aria-label="Green rising zigzag arrow illustration showing career growth"></div>
  </article>
</main>
</body>
</html>
```